New Corporate Email Signature with Custom GIF VAM Electric LLC & VAM Fire & Security

Project Overview
VAM Electric LLC and VAM Fire & Security are seeking a professional, polished, and technically robust corporate email signature design. The project has two integrated deliverables:
A custom animated GIF representing both sides of our business
A complete corporate email signature layout designed for real-world compatibility (Gmail, Outlook, iOS, Android)
Our brand aesthetic is corporate, conservative, and clean. We value clarity, trust, professionalism, and subtle creativity β€” nothing overly flashy or cartoonish.
This design will be used across the entire company and must be visually aligned with our brand while remaining technically dependable.

PART 1 β€” Animated GIF Requirements
The GIF will be the core visual anchor of the new signature.
It must be clean, smooth, subtle, and optimized for email use.
βš™ Technical Requirements
Max file size: 150–200 KB (smaller is better)
Dimensions: approx 300px width (flexible, but must look good small)
Looping: continuous loop
Style: professional, minimalistic transitions

No rapid flashing or harsh animations
Must export cleanly into a format email clients accept

🎞 GIF Animation Sequence
Phase 1 β€” VAM Electric (VE)
Use the yellow β€œVE” avatar logo (provided).
Animation flow:
VE avatar appears
Full name β€œVAM Electric LLC” slides in, fades in, or otherwise appears smoothly
A scrolling or cycling list of service offerings displays:
EV Charging Stations
Generator & Transformers
Testing & Troubleshooting
LED Lighting Upgrades
After the list is shown, the entire VE segment fades out

Phase 2 β€” VAM Fire & Security (VF)
Use the red β€œVF” avatar logo (provided).
Animation flow mirrors Phase 1:
VF avatar appears
Full name β€œVAM Fire & Security” slides/fades in
Scrolling or cycling list of services displays:
Fire Alarm Upgrades
KDLT 58 Test & Inspect
Security Surveillance Systems
Access Control Systems
Data & Fiber Optic Cabling
Fade out β†’ loop back to VE
Creative Direction

Designers are encouraged to use:
Clean transitions
Soft fades
Professional typography
Modern minimalism
Consistent brand colors
High clarity at small sizes

Avoid:
Busy motion
Hard flashes
Excessive text overlays
Overly long transitions

The goal: a smooth, corporate-grade rotation that fits seamlessly into an email signature.

PART 2 β€” Corporate Email Signature Design

The signature must be visually appealing, brand-aligned, and structurally bulletproof across all major email systems.
πŸ“ Required Elements
πŸ‘€ Left Side Content
Circular headshot (we will supply final photos)
Social media icons with embedded URLs:
Facebook
LinkedIn
Google Business Profile
Instagram

Icons should be clean, modern, and in alignment with brand colors
πŸ“„ Right Side Content
Name
Title
VAM Electric LLC / VAM Fire & Security (depending on user)
Phone number
Email address
License# 42860
Physical office address: 348 Brambleton Ave, Ferncliff NJ 07391

Small CTA for newsletter signup (button or micro-banner)

🏒 Branding Assets Provided

You will receive:
VE avatar logo
VF avatar logo
Full-name VE logo
Full-name VF logo

These should be incorporated naturally and professionally.

Design Requirements

Conservative corporate styling

Clean typography

Balanced use of white space

Professional hierarchy

Light and dark mode compatibility preferred

Layout should not rely on one large image

All images should export cleanly for hosting on servers/CDN

Avoid overly tall signatures

The final signature must present as modern, trustworthy, and technically reliable across platforms.

πŸ§ͺ Compatibility Requirements

The signature must display correctly in:

Gmail (web and mobile)

Outlook (desktop & online)

Apple Mail

iPhone Mail

Android mail apps

Designers must avoid DIV-based layouts and instead propose a layout that can be implemented using table-based HTML, which is the industry standard for email compatibility.

You do not need to build the HTML β€” only supply the final layered design (PSD/AI/Figma) plus a clear structural layout that can be converted to HTML later.

πŸ“¦ Deliverables
1. Animated GIF

Final optimized GIF

Source file (After Effects, Photoshop, or equivalent)

Export guidelines so we can reproduce future versions

2. Email Signature Design

Full static design mockup

Modular layout for each employee

Icon set for social media

Newsletter CTA element

Clear spacing, alignment, and typography specifications

All source files (PSD, AI, Figma, etc.)

🧭 Creative Guidance Summary

We want:
βœ” Modern
βœ” Corporate
βœ” Minimalistic
βœ” Professional
βœ” Clean motion
βœ” Consistent branding
βœ” Email-safe elements

We do not want:
✘ Flashy marketing look
✘ Overly colorful or playful styles
✘ Hard-to-read fonts
✘ Heavy animation
✘ Oversized signatures

πŸ›  Tools & Format Flexibility

We allow full creative freedom regarding:

Animation style

Typography choices

Structuring of the two-column layout

How the service lists scroll or cycle

As long as the end result is clean, brand-aligned, professional, and email-compatible.

πŸ’¬ Final Note to Designers

We encourage creativity within the boundaries of corporate professionalism.
This signature will represent our company every time an email is sent β€” it must communicate trust, clarity, expertise, and brand strength.

```html
<!DOCTYPE html>
<html lang="en">
<head>
<meta charset="utf-8">
<title>VAM Electric LLC – Email Signature</title>
<link rel="stylesheet" href="https://fonts.googleapis.com/css2?family=Open+Sans:wght@400;600;700&display=swap">
<style>
  :root {
    --stage: #d9d9d9;
    --paper: #ffffff;
    --ink: #767676;
    --ink-soft: #6b6b6b;
    --gold: #d8b32a;
    --caption: #6a6a6a;
  }
  * { box-sizing: border-box; margin: 0; padding: 0; }
  html, body { width: 1200px; height: 967px; overflow: hidden; }
  body {
    background: var(--stage);
    font-family: "Open Sans", Arial, sans-serif;
    position: relative;
  }
  .signature {
    position: absolute;
    left: 68px; top: 157px;
    width: 1067px; height: 378px;
    background: var(--paper);
    box-shadow: 0 10px 30px rgba(0,0,0,0.16);
  }
  .headshot {
    position: absolute;
    left: 44px; top: 35px;
    width: 205px; height: 205px;
    border-radius: 50%;
    background: radial-gradient(circle at 50% 40%, #efe9ee 0%, #e3dbe2 55%, #2c3550 100%);
  }
  .socials {
    position: absolute;
    left: 51px; top: 259px;
    display: flex; gap: 21px;
  }
  .socials a {
    display: block;
    width: 32px; height: 32px;
    border-radius: 50%;
    background: var(--gold);
  }
  .details {
    position: absolute;
    left: 290px; top: 0;
    color: var(--ink);
  }
  .details .name {
    position: absolute; top: 26px; left: -2px;
    font-size: 61px; font-weight: 700; white-space: nowrap;
    letter-spacing: -0.5px;
  }
  .details .title {
    position: absolute; top: 106px;
    font-size: 21px; font-weight: 400; white-space: nowrap;
  }
  .details .company {
    position: absolute; top: 140px;
    font-size: 26px; font-weight: 700; white-space: nowrap;
  }
  .company .accent, .label { color: var(--gold); }
  .contact {
    position: absolute; top: 205px;
    list-style: none;
    font-size: 20px; line-height: 39px;
    color: var(--ink-soft); white-space: nowrap;
  }
  .label { font-weight: 600; }
  .brand-block {
    position: absolute;
    left: 740px; top: 193px;
    width: 300px;
    text-align: center;
  }
  .brand-name {
    font-size: 30px; line-height: 34px; font-weight: 700; color: var(--ink);
    white-space: nowrap;
  }
  .brand-tagline {
    margin-top: 2px;
    font-size: 19px; line-height: 24px; font-weight: 700; color: var(--ink);
    white-space: nowrap;
  }
  .newsletter {
    position: absolute;
    left: 778px; top: 320px;
    width: 233px; height: 33px;
    border-radius: 3px;
    background: var(--gold);
    color: #fff;
    font-size: 20px; font-weight: 700;
    text-align: center; line-height: 33px;
    text-decoration: none;
    white-space: nowrap;
  }
  .gif-frame {
    position: absolute;
    left: 479px; top: 685px;
    width: 282px; height: 188px;
    background: var(--paper);
    text-align: center;
    padding-top: 93px;
  }
  .gif-frame .brand-name { font-size: 27px; line-height: 32px; }
  .gif-frame .brand-tagline { font-size: 18px; line-height: 22px; margin-top: 5px; }
  .gif-caption {
    position: absolute;
    left: 479px; top: 888px; width: 282px;
    text-align: center;
    font-size: 14px; color: var(--caption);
  }
</style>
</head>
<body>
  <section class="signature">
    <div class="headshot" role="img" aria-label="Circular headshot of the employee"></div>
    <nav class="socials" aria-label="Social profiles">
      <a href="#" aria-label="Photo sharing profile"></a>
      <a href="#" aria-label="Community page"></a>
      <a href="#" aria-label="Professional network profile"></a>
      <a href="#" aria-label="Business listing"></a>
    </nav>
    <div class="details">
      <h1 class="name">Daniel Reyes</h1>
      <p class="title">Project Manager</p>
      <p class="company">VAM <span class="accent">Electric LLC</span></p>
      <ul class="contact">
        <li><span class="label">P :</span> 555-014-2286</li>
        <li><span class="label">E :</span>&nbsp; daniel.reyes@vamelectric.com</li>
        <li><span class="label">License</span> # 42860</li>
        <li><span class="label">Office</span> 348 Brambleton Ave, Ferncliff NJ 07391</li>
      </ul>
    </div>
    <div class="brand-block">
      <p class="brand-name">VAM Electric LLC</p>
      <p class="brand-tagline">EV Charging Stations</p>
    </div>
    <a class="newsletter" href="#">Join Our Newsletter</a>
  </section>

  <div class="gif-frame">
    <p class="brand-name">VAM Electric LLC</p>
    <p class="brand-tagline">EV Charging Stations</p>
  </div>
  <p class="gif-caption">GIF - 300px</p>
</body>
</html>
```